ReDesign of Velmarix.example and Velmarix app

Velmarix:

Velmarix aims to be your own personal cloud of profile information with ability to share a part of it with others based on the consumer.

As we visit different sites and buy different products, apply for new jobs, on-board in a company or fill out a basic form at a doctors office, we end up entering the same information again and again albeit with some sections different based on where you are. For example, we enter some basic informaiton “AND” billing address on brindle, vs you enter some basic information “AND” work history on a job site.

What if you created a profile one time and then create justed avatars or keys to a combination of information and at different places use different keys to unlock that specific piece of information.

Use Case 1: Peter Hale applying for a job
Peter goes to task harbor, creates new login, enters where he lives, email, phone, then goes into the most tedious phase of entering work history. He realizes, he also needs to go to Quillrun.example and do the exact same thing and so on on any job site he visits in future.

With Velmarix
Peter goes to Velmarix, updates all his work history, personal information (No SSN or credit card). Now he creates a new “key” called “petersworkrequest” with a cryptic “keycode” and chooses to share personal information + work history for this key. He now goes to any job site to see a “VX” icon. He clicks on that, a pop-up box with key and keycode appears. He ONLY enters petersworkrequset and the keycode he had set, boom, all his work informaiton is auto-populated in task harbor. Immense savings in time for Peter.

Use Case 2: Sharing contact information
Peter meets a beautiful at a bar and thinks he needs to share his personal information but only has a 5 mintue window. He realizes, he has created a key named “Peter42” and has chosen to share his personal information only (no work information). She asks for contact number, he gives her is VX key. She pulls up VX app instead of contact list to add contact, plugs in Peter42 (and a key if peter decides to protect this key with a code) and boom, she has peters phone/email/picture (yes picture), chatterly blog and a contact is automatically created!!!!! She now can really associate this Peter from 8 other Peter’s in the bar!!

Use Case 3: Always stay connected
Peter is bored of Houston and decides to move to LA.He wants a local phone number for people to get in touch with them easily. But now he has to do the painful job of sending all his friends his updated number/contact address. If he had exchanged information with Velmarix key with his friends, his contact information with them is always in sync. TThe Velmarix app is intelligent to know that new information is available for the same profile key. As long as the passcode is the same, that information is automatically updated in the consumers contact list. Next time Peter’s friend picks up the phone, he just need so hit “DIAL”. The correct number is dialed. Along with that, his friends now also have his updated address information which he had shared with the key.

SECURITY
Anytime anyone views your profile using your profile key, you automatically get notified to your registered email address of someone pulling up your profile. If you think it’s suspicious, you can change the access code or set an access code to that public key.

where to go:
Go to http://velmarix.example
Register and play around with different views you can create for your profile with different access codes

Download
Velmarix app from pomelo appshelf or Vantor playshelf. We need a nice look and feel for the app as well.

Target Market(s)

students, careers, hiring companies, anyone starting online presence

Industry/Entity Type

Credit Card

Requirements
Must have

• convey message, simplistic, an app to consume data, always stay updated with friends emails etc
Nice to have
• logo should show a user and multiple facets of user for multiple consumers

```html
<!DOCTYPE html>
<html lang="en">
<head>
<meta charset="utf-8">
<title>Velmarix — Your job search starts here</title>
<link rel="stylesheet" href="https://fonts.googleapis.com/css2?family=Source+Sans+3:wght@400;600;700&family=Oswald:wght@400&family=Arimo:ital,wght@0,400;1,700&display=swap">
<style>
:root{
  --green:#9cc21b;
  --green-dark:#7fa50f;
  --green-light:#b5d62a;
  --grey-text:#9a9a9a;
  --grey-dark:#555;
  --page:#f6f6f6;
  --footer:#8a8a8a;
  --black:#141414;
  --white:#ffffff;
}
*{margin:0;padding:0;box-sizing:border-box}
html,body{width:1200px;height:1076px;overflow:hidden}
body{position:relative;background:var(--page);font-family:"Source Sans 3",sans-serif;color:var(--grey-dark)}
.abs{position:absolute}
.top-bar{left:0;top:0;width:1200px;height:4px;background:var(--green)}
.corner-tab{right:0;top:0;width:44px;height:44px}
.login-link{left:1084px;top:16px;font-size:15px;color:var(--green);text-decoration:none}
.social-row{display:flex;gap:9px}
.social-row span{width:14px;height:14px;border-radius:50%;background:#333;display:block}
.header-social{left:724px;top:19px}
.logo{left:182px;top:40px;font-size:45px;font-weight:700;color:#8c8c8c;letter-spacing:-1px}
.logo sup{font-size:13px;color:#555;vertical-align:30px;margin-left:2px}
.main-nav{left:457px;top:62px;display:flex;font-size:16px}
.main-nav a{color:var(--grey-text);text-decoration:none;padding:0 15px;border-left:1px dashed #ccc}
.main-nav a:first-child{border:none;padding-left:0;color:var(--green)}
.find-btn{left:876px;top:51px;width:148px;height:40px;border-radius:4px;background:linear-gradient(var(--green-light),var(--green-dark));border:1px solid #8ab015;color:var(--white);font-size:16px;display:flex;align-items:center;justify-content:center;gap:8px}
.header-rule{left:171px;top:112px;width:860px;height:8px;background:radial-gradient(ellipse at top,rgba(0,0,0,.08),transparent 70%)}
.hero-visual{left:171px;top:120px;width:540px;height:326px;background:radial-gradient(ellipse at 55% 45%,#f2e0d0 0%,#d9d9d9 45%,#f0f0f0 80%);border-radius:4px}
.headline{left:714px;top:135px;line-height:1}
.headline .lead{font-size:35px;color:var(--green);display:block;font-weight:600}
.headline .big{font-size:54px;color:#a9a9a9;display:block;font-weight:600;margin-top:2px;letter-spacing:-.5px}
.mark-vx{left:878px;top:138px;font-size:68px;font-weight:700;color:var(--green)}
.download-label{left:782px;top:355px;font-size:23px;color:#b0b0b0}
.store-badge{height:41px;border-radius:5px;background:#000;border:1px solid #555;color:var(--white);font-size:15px;display:flex;align-items:center;justify-content:center}
.badge-play{left:736px;top:393px;width:125px}
.badge-shelf{left:896px;top:393px;width:126px}
.or-label{left:865px;top:402px;font-size:17px;color:var(--green)}
.works-panel{left:158px;top:447px;width:545px;height:275px;background:linear-gradient(#b9d82b,#92b90f)}
.connect-panel{left:703px;top:447px;width:343px;height:275px;background:linear-gradient(#a6a6a6,#505050)}
.panel-shadow{left:158px;top:722px;width:888px;height:16px;background:radial-gradient(ellipse at top,rgba(0,0,0,.25),transparent 70%)}
.panel-title{font-size:28px;font-weight:600;color:var(--white);text-shadow:0 1px 2px rgba(0,0,0,.3)}
.step{width:140px;text-align:center;top:510px}
.step-circle{width:132px;height:132px;border-radius:50%;margin:0 auto;background:radial-gradient(circle at 50% 35%,#333,#000 70%);box-shadow:0 3px 6px rgba(0,0,0,.4);color:var(--white);display:flex;flex-direction:column;align-items:center;padding-top:26px;gap:12px}
.step-circle .brand{font-size:13px;font-weight:600;color:#ddd}
.step-label{font-size:16px;color:#2a2a2a;line-height:18px;margin-top:10px;text-transform:uppercase}
.chevron{top:556px}
.field{left:733px;width:294px;height:28px;border-radius:14px;background:linear-gradient(#fff,#e8e8e8);font-size:15px;color:#222;padding-left:17px;line-height:28px}
.create-btn{left:733px;top:662px;width:283px;height:44px;border-radius:22px;background:var(--black);color:var(--white);font-size:21px;font-weight:600;display:flex;align-items:center;justify-content:center;gap:12px;box-shadow:0 2px 4px rgba(0,0,0,.4)}
.section-title{font-size:22px;font-weight:600;color:var(--green-dark)}
.section-title sup{font-size:12px;color:#333}
.body-copy{font-family:Arimo,sans-serif;font-size:10.4px;line-height:18px;color:#666}
.quote-mark{font-family:Georgia,serif;font-size:22px;color:var(--green-dark);font-weight:700}
.author{left:900px;top:858px;font-family:Arimo,sans-serif;font-style:italic;font-weight:700;font-size:10.5px;color:var(--green-dark)}
.site-footer{left:0;top:897px;width:1200px;height:179px;background:linear-gradient(#8f8f8f,#7e7e7e)}
.foot-col{top:922px}
.foot-col h3{font-family:Oswald,sans-serif;font-weight:400;font-size:16px;color:var(--white);margin-bottom:10px}
.foot-col a{display:block;font-family:Arimo,sans-serif;font-size:10.5px;color:var(--white);text-decoration:none;line-height:20px}
.footer-social{left:814px;top:924px}
.footer-social span{background:#eee}
.footer-logo{left:756px;top:942px;font-size:44px;font-weight:700;color:var(--white);letter-spacing:-1px}
.footer-logo sup{font-size:12px;vertical-align:28px;color:#eee}
.copyright{left:730px;top:1010px;width:280px;text-align:center;font-family:Arimo,sans-serif;font-size:10.5px;line-height:21px;color:var(--white)}
</style>
</head>
<body>
<div class="abs top-bar"></div>
<svg class="abs corner-tab" viewBox="0 0 44 44"><polygon points="0,0 44,0 44,44" fill="#a9cc1f"/><rect x="30" y="10" width="8" height="7" rx="1" fill="#fff"/><path d="M31.5 10v-2a2.5 2.5 0 0 1 5 0v2" stroke="#fff" stroke-width="1.3" fill="none"/></svg>
<a class="abs login-link" href="#">LOGIN HERE</a>
<div class="abs social-row header-social" aria-label="Social links"><span></span><span></span><span></span><span></span><span></span></div>

<header>
  <div class="abs logo">Velmarix<sup>VX</sup></div>
  <nav class="abs main-nav"><a href="#">HOME</a><a href="#">ABOUT US</a><a href="#">MY PROFILE</a><a href="#">APPSTORE</a></nav>
  <div class="abs find-btn"><svg width="14" height="14" viewBox="0 0 14 14"><circle cx="5.5" cy="5.5" r="4" stroke="#fff" stroke-width="2" fill="none"/><line x1="8.5" y1="8.5" x2="13" y2="13" stroke="#fff" stroke-width="2.4"/></svg>FIND PROFILE</div>
  <div class="abs header-rule"></div>
</header>

<section class="hero">
  <div class="abs hero-visual" role="img" aria-label="Smiling young professional presenting a laptop showing a profile dashboard, with floating profile cards"></div>
  <h1 class="abs headline"><span class="lead">YOUR</span><span class="big">JOB</span><span class="big">SEARCH</span><span class="big">STARTS HERE</span></h1>
  <div class="abs mark-vx">VX</div>
  <div class="abs download-label">DOWNLOAD FROM</div>
  <div class="abs store-badge badge-play">Vantor playshelf</div>
  <div class="abs or-label">OR</div>
  <div class="abs store-badge badge-shelf">pomelo appshelf</div>
</section>

<section class="how-it-works">
  <div class="abs works-panel"></div>
  <h2 class="abs panel-title" style="left:216px;top:462px">HOW IT WORKS?</h2>
  <div class="abs step" style="left:197px">
    <div class="step-circle"><span class="brand">Velmarix</span>
      <svg width="48" height="40" viewBox="0 0 48 40"><rect x="2" y="2" width="44" height="30" fill="#fff"/><rect x="6" y="6" width="36" height="22" fill="#000"/><rect x="18" y="32" width="12" height="4" fill="#fff"/><rect x="12" y="36" width="24" height="3" fill="#fff"/><circle cx="30" cy="14" r="4" fill="#fff"/><path d="M22 27a8 7 0 0 1 16 0z" fill="#fff"/><path d="M10 14h8M14 10v8" stroke="#fff" stroke-width="3"/></svg>
    </div>
    <div class="step-label">Create<br>Profile</div>
  </div>
  <svg class="abs chevron" style="left:336px" width="24" height="40" viewBox="0 0 24 40"><path d="M2 2l14 18-14 18M8 2l14 18-14 18" stroke="#111" stroke-width="4" fill="none"/></svg>
  <div class="abs step" style="left:359px;width:140px">
    <div class="step-circle"><span class="brand">Velmarix</span>
      <svg width="52" height="38" viewBox="0 0 52 38"><rect x="1" y="1" width="50" height="36" rx="3" fill="#ddd"/><rect x="1" y="12" width="50" height="5" fill="#555"/><rect x="6" y="24" width="24" height="3" fill="#777"/><rect x="6" y="30" width="16" height="3" fill="#777"/><circle cx="42" cy="24" r="4" fill="#333"/><path d="M35 35a7 6 0 0 1 14 0z" fill="#333"/></svg>
    </div>
    <div class="step-label">Share Contact<br>Information</div>
  </div>
  <svg class="abs chevron" style="left:500px" width="24" height="40" viewBox="0 0 24 40"><path d="M2 2l14 18-14 18M8 2l14 18-14 18" stroke="#111" stroke-width="4" fill="none"/></svg>
  <div class="abs step" style="left:524px">
    <div class="step-circle"><span class="brand">Velmarix</span>
      <svg width="46" height="40" viewBox="0 0 46 40"><path d="M3 14a28 28 0 0 1 40 0M9 20a19 19 0 0 1 28 0M15 26a10 10 0 0 1 16 0" stroke="#fff" stroke-width="4" fill="none"/><rect x="17" y="30" width="12" height="6" fill="#fff"/><rect x="13" y="36" width="20" height="3" fill="#fff"/></svg>
    </div>
    <div class="step-label">Always Stay<br>Connected</div>
  </div>
</section>

<section class="get-connected">
  <div class="abs connect-panel"></div>
  <h2 class="abs panel-title" style="left:734px;top:462px">GET CONNECTED</h2>
  <div class="abs field" style="top:510px">USERNAME</div>
  <div class="abs field" style="top:543px">EMAIL</div>
  <div class="abs field" style="top:577px">PASSWORD</div>
  <div class="abs field" style="top:610px">CONFIRM PASSWORD</div>
  <div class="abs create-btn">CREATE PROFILE NOW!<svg width="14" height="22" viewBox="0 0 14 22"><path d="M2 2l9 9-9 9" stroke="#fff" stroke-width="3" fill="none"/></svg></div>
</section>
<div class="abs panel-shadow"></div>

<section class="about">
  <h2 class="abs section-title" style="left:181px;top:745px">What is Velmarix<sup>VX</sup> ?</h2>
  <p class="abs body-copy" style="left:183px;top:787px;width:500px">Lorem ipsum dolor sit amet, consectetuer adipiscing elit, sed diam nonummy nibh euismod tincidunt ut laoreet dolore magna aliquam erat volutpat. Ut wisi enim ad minim veniam, quis nostrud exerci tation ullamcorper suscipit lobortis nisl ut aliquip ex ea commodo consequat. Duis autem vel eum iriure dolor in hendrerit in vulputate velit esse molestie consequat, vel illum dolore eu feugiat nulla.</p>
</section>

<section class="testimonials">
  <h2 class="abs section-title" style="left:719px;top:745px">TESTIMONIALS</h2>
  <span class="abs quote-mark" style="left:720px;top:785px">“</span>
  <p class="abs body-copy" style="left:738px;top:787px;width:282px">Lorem ipsum dolor sit amet, consectetuer adipiscing elit, sed diam nonummy nibh euismod tincidunt ut laoreet dolore magna aliquam erat volutpat. Ut wisi enim ad minim veniam...</p>
  <span class="abs quote-mark" style="left:801px;top:836px">”</span>
  <div class="abs author">Mara Quill, Dunmore</div>
</section>

<footer class="abs site-footer"></footer>
<div class="abs foot-col" style="left:193px"><h3>WHO WE ARE</h3><a href="#">Company</a><a href="#">News</a><a href="#">Team</a><a href="#">Careers</a><a href="#">Contact</a></div>
<div class="abs foot-col" style="left:351px"><h3>WHAT WE DO</h3><a href="#">What is Velmarix?</a><a href="#">Live Demo</a><a href="#">Resources</a><a href="#">FAQs</a><a href="#">Mobile Apps</a></div>
<div class="abs foot-col" style="left:531px"><h3>WHO WE WORK WITH</h3><a href="#">Utilities</a><a href="#">Consumers</a><a href="#">Partners</a><a href="#">Get Started</a></div>
<div class="abs social-row footer-social" aria-label="Social links"><span></span><span></span><span></span><span></span><span></span></div>
<div class="abs footer-logo">Velmarix<sup>VX</sup></div>
<p class="abs copyright">2006 - 2013 &nbsp; Velmarix VX Privacy Policy Terms of Conditions. All Rights Reserved</p>
</body>
</html>
```